Time for a new business card design

We need a new business card design for Tolvik Furniture Rentals based in Australia. www.tolvik-example.com.au. We specialise in providing furniture rentals for home staging, corporate relocations events and product launches etc. We would like to see designs that include our logo on the front of the card with all the standard contact details as well as having a realy nice image on the back with a list of our services we offer. Our logo is red and this cannot change. Were looking for a pallet of red and white with maybe a splash of grey. The final design should communication organised & stylish. We are in the process of finalising our new website and would like the card design to compliment this as well

Requirements
Must have
• Square corners
logo
name, title, email, phone, address
image on back of card with space for list of services we offer
Services:
•Furniture and appliance rental
•Property styling
•Events and functions
•Office furniture rental

The card must be landscape.
The image is to appear on the back of the card only.

```html
<!DOCTYPE html>
<html lang="en">
<head>
<meta charset="utf-8">
<title>Tolvik Furniture Rentals – Business Card</title>
<link rel="stylesheet" href="https://fonts.googleapis.com/css2?family=Lato:wght@300;400;700&display=swap">
<style>
  :root {
    --brand-red: #b8262b;
    --brand-red-light: #c63a3c;
    --paper: #ffffff;
    --ink-grey: #5a5a5a;
    --rule-grey: #9a9a9a;
    --stage: #e9ecee;
    --photo-sky: #8fbfe6;
    --photo-room: #e4e6e8;
    --photo-bed: #f4f4f4;
  }
  * { box-sizing: border-box; margin: 0; padding: 0; }
  html, body {
    width: 1200px; height: 960px; overflow: hidden;
    background: var(--stage);
    font-family: "Lato", sans-serif;
  }
  .sheet {
    width: 1200px; height: 960px;
    display: flex; flex-direction: column;
    align-items: center; justify-content: center; gap: 60px;
  }
  .card {
    width: 600px; height: 343px;
    background: var(--paper);
    position: relative; overflow: hidden;
    box-shadow: 0 4px 18px rgba(0,0,0,0.12);
  }
  /* Front */
  .card-front__band {
    height: 158px;
    background: linear-gradient(90deg, var(--brand-red), var(--brand-red-light));
    display: flex; align-items: flex-end;
    padding: 0 30px 38px;
  }
  .brand-name {
    color: var(--paper);
    font-weight: 300;
    font-size: 44px;
    letter-spacing: -0.5px;
    line-height: 1;
    white-space: nowrap;
  }
  .card-front__details { padding: 44px 30px 0; color: var(--ink-grey); }
  .person {
    font-size: 25px; font-weight: 400;
    padding-bottom: 8px;
    border-bottom: 1.5px solid var(--rule-grey);
    width: 360px;
    white-space: nowrap;
  }
  .person__title { font-size: 16px; }
  .contact-row {
    display: flex; align-items: center; gap: 12px;
    margin-top: 12px; font-size: 13px;
    white-space: nowrap;
  }
  .contact-item { display: flex; align-items: center; gap: 6px; flex: none; }
  .contact-item svg { width: 14px; height: 14px; flex: none; }
  .address { margin-top: 9px; font-size: 14px; white-space: nowrap; }
  /* Back */
  .card-back__photo {
    position: absolute; inset: 0;
    background:
      linear-gradient(180deg, var(--photo-sky) 0%, var(--photo-sky) 12%, var(--photo-room) 12%, var(--photo-room) 40%, var(--photo-bed) 40%, var(--photo-bed) 100%);
  }
  .card-back__services {
    position: absolute; left: 24px; right: 24px; bottom: 30px;
    background: rgba(255,255,255,0.82);
    padding: 8px 12px;
    text-align: center;
    color: var(--brand-red);
    font-size: 15px; line-height: 1.35; letter-spacing: 0.3px;
  }
</style>
</head>
<body>
<main class="sheet">
  <section class="card card-front" aria-label="Business card front">
    <div class="card-front__band">
      <span class="brand-name">Tolvik Furniture Rentals</span>
    </div>
    <div class="card-front__details">
      <p class="person">Name Surname <span class="person__title">/ Operation Manager</span></p>
      <div class="contact-row">
        <span class="contact-item">
          <svg viewBox="0 0 14 14" aria-hidden="true"><rect x="1" y="1" width="12" height="12" rx="1.5" fill="none" stroke="var(--brand-red)" stroke-width="1.6"/><rect x="3.5" y="3" width="2" height="8" fill="var(--brand-red)"/><rect x="7" y="3.5" width="4" height="2" fill="var(--brand-red)"/><rect x="7" y="7" width="1.5" height="1.5" fill="var(--brand-red)"/><rect x="9.5" y="7" width="1.5" height="1.5" fill="var(--brand-red)"/><rect x="7" y="9.3" width="1.5" height="1.5" fill="var(--brand-red)"/><rect x="9.5" y="9.3" width="1.5" height="1.5" fill="var(--brand-red)"/></svg>
          1800 55 01 99
        </span>
        <span class="contact-item">
          <svg viewBox="0 0 14 14" aria-hidden="true"><rect x="1" y="2.5" width="12" height="9" fill="none" stroke="var(--brand-red)" stroke-width="1.5"/><path d="M1 2.5 L7 8 L13 2.5 M1 11.5 L5.5 7 M13 11.5 L8.5 7" fill="none" stroke="var(--brand-red)" stroke-width="1.3"/></svg>
          info@tolvik-example.com.au
        </span>
        <span class="contact-item">
          <svg viewBox="0 0 14 14" aria-hidden="true"><circle cx="7" cy="7" r="6" fill="var(--brand-red)"/><path d="M4 4.5 Q6 3.5 7 5.5 Q6 7 7.5 8 Q9 9.5 8 11.5 M9.5 3 Q10.5 5 9.5 6" fill="none" stroke="#fff" stroke-width="1.2"/></svg>
          www.tolvik-example.com.au
        </span>
      </div>
      <p class="address">Marlow Avenue 48 - Ridgeview, PO 375 - City, Country</p>
    </div>
  </section>

  <section class="card card-back" aria-label="Business card back">
    <div class="card-back__photo" role="img" aria-label="Photo of a bright styled bedroom with white bedding, patterned cushions, a lamp and an ocean view through the window"></div>
    <p class="card-back__services">
      Furniture and appliance rental | Property styling | Events and functions<br>
      Office furniture rental
    </p>
  </section>
</main>
</body>
</html>
```